Www.zapdeck.com monthly sweepstakes.

Every month I am giving away 1st place $500 gift card to your local RC hobby shop of choice, 2nd place $100 gift card 3rd place ZapDeck merch. All things rc: cars, boats, quadcopters, helicopters, airplanes.

Needs to be with the color theme of the website. Check zapdeck.com for current sweepstakes banner. New banner should be half the size in height. I will post dimension later.

Target Market(s)

Rc hobbies cars airplanes helicopters boats

Industry/Entity Type

RemoteControl hobbies

Requirements
Must have
• 1440x680 size, Blend with black background, creative and in incorporate all trypes of rc craft
Should not have
• To many different colors, dosnt need logo as its already on website. This is a banner for my homepage

```html
<!DOCTYPE html>
<html lang="en">
<head>
<meta charset="UTF-8">
<title>ZapDeck Monthly Sweepstakes Banner</title>
<link href="https://fonts.googleapis.com/css2?family=League+Gothic&family=Poppins:wght@500;600;700&display=swap" rel="stylesheet">
<style>
  :root {
    --bg: #0b0b0c;
    --gold-light: #ffd45a;
    --gold: #f1a928;
    --gold-dark: #b9781a;
    --red: #e0112b;
    --red-dark: #a80a1e;
    --silver-light: #ffffff;
    --silver: #cfcfd2;
    --ink: #1a1a1a;
    --white: #ffffff;
    --vehicle-light: #e6a030;
    --vehicle-dark: #2a2420;
  }
  * { margin: 0; padding: 0; box-sizing: border-box; }
  html, body { width: 1200px; height: 567px; overflow: hidden; background: var(--bg); }
  .banner {
    position: relative;
    width: 1200px;
    height: 567px;
    overflow: hidden;
    background:
      linear-gradient(105deg, transparent 0 14%, rgba(255,255,255,0.025) 14% 15%, transparent 15% 84%, rgba(255,255,255,0.025) 84% 85%, transparent 85%),
      radial-gradient(ellipse at 50% 45%, #1c1c1f 0%, var(--bg) 70%);
    font-family: "Poppins", sans-serif;
  }
  .accent-lines { position: absolute; inset: 0; }
  .title-row {
    position: absolute;
    top: 46px;
    left: 0;
    width: 100%;
    height: 80px;
    display: flex;
    align-items: center;
    justify-content: center;
    gap: 18px;
    z-index: 2;
  }
  .headline {
    font-family: "League Gothic", sans-serif;
    font-weight: 400;
    font-size: 98px;
    line-height: 80px;
    letter-spacing: 0.5px;
    white-space: nowrap;
    background: linear-gradient(180deg, var(--gold-light) 0%, var(--gold) 50%, var(--gold-dark) 100%);
    -webkit-background-clip: text;
    background-clip: text;
    color: transparent;
  }
  .popper {
    flex: 0 0 auto;
    width: 64px;
    height: 68px;
    border-radius: 10px;
    background: linear-gradient(135deg, #3aa0e8, #f0b43a 55%, #e8408a);
    opacity: 0.85;
  }
  .vehicle {
    position: absolute;
    left: 304px;
    top: 132px;
    width: 600px;
    height: 300px;
    border-radius: 60px 90px 40px 40px;
    background: linear-gradient(180deg, #333 0%, var(--vehicle-light) 28%, #c98722 60%, var(--vehicle-dark) 78%, #151515 100%);
  }
  .prize { position: absolute; top: 408px; width: 236px; height: 130px; z-index: 3; }
  .prize--first { left: 189px; }
  .prize--second { left: 486px; }
  .prize--third { left: 783px; }
  .prize__rank {
    position: absolute;
    left: 0;
    top: 0;
    width: 54px;
    height: 54px;
    border-radius: 50%;
    background: radial-gradient(circle at 40% 35%, var(--gold-light), var(--gold) 55%, var(--gold-dark));
    border: 2px solid #fff0c0;
    color: var(--ink);
    font-weight: 700;
    font-size: 18px;
    display: flex;
    align-items: center;
    justify-content: center;
    z-index: 3;
  }
  .prize__rank sup { font-size: 11px; margin-left: 1px; }
  .prize__value {
    position: absolute;
    left: 40px;
    top: 10px;
    width: 120px;
    height: 40px;
    background: linear-gradient(180deg, var(--red), var(--red-dark));
    clip-path: polygon(0 0, 100% 0, 94% 100%, 0 100%);
    color: var(--white);
    font-weight: 700;
    font-size: 25px;
    line-height: 40px;
    padding-left: 24px;
    z-index: 2;
  }
  .prize__value--brand { font-size: 17px; font-weight: 600; padding-left: 22px; }
  .prize__label {
    position: absolute;
    left: 28px;
    top: 42px;
    width: 170px;
    height: 52px;
    padding-top: 6px;
    background: linear-gradient(180deg, var(--silver-light), var(--silver));
    clip-path: polygon(4% 0, 100% 0, 96% 100%, 0 100%);
    color: var(--ink);
    font-weight: 500;
    font-size: 19px;
    line-height: 44px;
    text-align: center;
  }
  .prize__label--small { font-size: 15px; }
  .prize__trophy {
    position: absolute;
    left: 194px;
    top: 6px;
    width: 36px;
    height: 50px;
    border-radius: 6px 6px 10px 10px;
    background: linear-gradient(180deg, var(--gold-light), var(--gold-dark) 70%, #7a3a5a);
  }
  .prize__note {
    position: absolute;
    left: 20px;
    top: 102px;
    width: 190px;
    text-align: center;
    color: var(--white);
    font-size: 14px;
    font-weight: 500;
    white-space: nowrap;
  }
</style>
</head>
<body>
  <main class="banner">
    <svg class="accent-lines" width="1200" height="567" viewBox="0 0 1200 567" aria-hidden="true">
      <line x1="1090" y1="0" x2="1200" y2="36" stroke="#e0112b" stroke-width="2" opacity="0.9"/>
      <line x1="1070" y1="0" x2="1200" y2="42" stroke="#e0112b" stroke-width="8" opacity="0.15"/>
      <line x1="40" y1="520" x2="125" y2="567" stroke="#e0112b" stroke-width="2" opacity="0.9"/>
      <line x1="30" y1="515" x2="125" y2="567" stroke="#e0112b" stroke-width="8" opacity="0.15"/>
      <line x1="120" y1="480" x2="105" y2="567" stroke="#e0112b" stroke-width="1.5" opacity="0.7"/>
    </svg>

    <div class="title-row">
      <div class="popper" role="img" aria-label="Party popper with confetti"></div>
      <h1 class="headline">WIN AN RC SHOPPING SPREE!</h1>
      <div class="popper" role="img" aria-label="Party popper with confetti"></div>
    </div>

    <div class="vehicle" role="img" aria-label="Orange RC off-road crawler truck with large tires"></div>

    <section class="prize prize--first">
      <div class="prize__rank">1<sup>st</sup></div>
      <div class="prize__value">$500</div>
      <div class="prize__label">GIFT CARD</div>
      <div class="prize__trophy" role="img" aria-label="Gold trophy"></div>
      <p class="prize__note">to your local hobby shop</p>
    </section>

    <section class="prize prize--second">
      <div class="prize__rank">2<sup>nd</sup></div>
      <div class="prize__value">$100</div>
      <div class="prize__label">GIFT CARD</div>
      <div class="prize__trophy" role="img" aria-label="Gold trophy"></div>
    </section>

    <section class="prize prize--third">
      <div class="prize__rank">3<sup>rd</sup></div>
      <div class="prize__value prize__value--brand">ZapDeck</div>
      <div class="prize__label prize__label--small">ZapDeck Merch</div>
      <div class="prize__trophy" role="img" aria-label="Gold trophy"></div>
    </section>
  </main>
</body>
</html>
```